TRELLWICK Construction Group business card for distribution

A business card detailing our services, with our phone number and email address.
- Groundworks / Foundations / Drainage
- Landscaping / Hard Landscaping / Patios / Decking
- Fencing
The card should include company logo and be in the same colours.

Target Market(s)
Domestic Houses
Industry/Entity Type
Construction
Contact Information for Business Card
Phone Number - 07931 258 904 / 07713829516. Email address: trellgroup@stonevane-mail.com
Font styles to use
Serif
Sans Serif
Colors
F0912C
F2A743
F7CA91
FBE8D2
FDF5EE
Requirements
Must have
- Contact numbers. Photos of past work. Company Logo

Nice to have
- Company Logo

```html
<!DOCTYPE html>
<html lang="en">
<head>
<meta charset="utf-8">
<title>TRELLWICK Construction Group – Business Card</title>
<link rel="stylesheet" href="https://fonts.googleapis.com/css2?family=Josefin+Sans:wght@400;600;700&family=Montserrat:wght@600;800&display=swap">
<style>
  :root {
    --backdrop: #959595;
    --card-dark: #221f20;
    --card-light: #ffffff;
    --orange: #f7961f;
    --grey-shape: #bfc0c2;
    --service-text: #b9b9b9;
    --ink: #1d1d1d;
    --title-grey: #8c8c8c;
  }
  * { margin: 0; padding: 0; box-sizing: border-box; }
  html, body { width: 1200px; height: 1000px; overflow: hidden; }
  body { background: var(--backdrop); position: relative; font-family: "Josefin Sans", sans-serif; }

  .card {
    position: absolute; left: 253px; width: 694px; height: 400px;
    border-radius: 16px; overflow: hidden;
    box-shadow: 14px 16px 22px rgba(0,0,0,0.35);
  }
  .card--front { top: 61px; background: var(--card-dark); }
  .card--back { top: 523px; background: var(--card-light); }

  /* wordmark */
  .wordmark { position: absolute; text-align: center; font-family: "Montserrat", sans-serif; }
  .wordmark__name {
    display: flex; align-items: center; justify-content: center; gap: 10px;
    font-weight: 800; font-size: 50px; letter-spacing: 1px; line-height: 1;
  }
  .wordmark__dot { width: 28px; height: 28px; background: var(--orange); }
  .wordmark__sub { font-weight: 600; font-size: 13px; letter-spacing: 1px; margin-top: 8px; }

  .card--front .wordmark { left: 0; right: 0; top: 46px; color: #ffffff; }
  .card--back .wordmark { left: 395px; width: 235px; top: 82px; color: var(--ink); }
  .card--back .wordmark__name { font-size: 36px; gap: 8px; }
  .card--back .wordmark__dot { width: 20px; height: 20px; }
  .card--back .wordmark__sub { font-size: 12px; margin-top: 6px; }

  /* project photos */
  .gallery { position: absolute; left: 0; top: 162px; width: 694px; height: 165px; display: flex; }
  .gallery__photo { flex: 1; height: 100%; }
  .gallery__photo--fence { background: linear-gradient(180deg, #6f8a4a 0%, #8d8a6a 55%, #b9ab86 100%); }
  .gallery__photo--alley { background: linear-gradient(180deg, #8fb0d4 0%, #a5a7ab 45%, #4c4e52 100%); }
  .gallery__photo--wall { background: linear-gradient(180deg, #9cb7d6 0%, #c7cacc 40%, #7c7f82 100%); }
  .gallery__photo--deck { background: linear-gradient(180deg, #8ea3b8 0%, #b3b0aa 40%, #a9865c 100%); }
  .gallery__photo--site { background: linear-gradient(180deg, #b0c6dd 0%, #a7a8aa 45%, #8b8175 100%); }

  .services {
    position: absolute; left: 0; right: 0; top: 345px;
    text-align: center; color: var(--service-text);
    font-size: 16px; letter-spacing: 1.3px; line-height: 20px; text-transform: uppercase;
  }
  .services__sep { color: var(--orange); }

  /* back decoration */
  .back-art { position: absolute; left: 0; top: 0; }

  .contact { position: absolute; left: 375px; width: 275px; top: 186px; text-align: center; }
  .contact__name { color: var(--orange); font-weight: 700; font-size: 21px; letter-spacing: 1.5px; }
  .contact__title { color: var(--title-grey); font-size: 21px; margin-top: 4px; letter-spacing: 0.5px; }
  .contact__icons { display: flex; justify-content: center; gap: 3px; margin-top: 8px; }
  .contact__icon { width: 23px; height: 23px; }
  .contact__line { color: var(--ink); font-size: 16px; letter-spacing: 0.8px; margin-top: 6px; }
  .contact__line + .contact__line { margin-top: 4px; }
</style>
</head>
<body>

<section class="card card--front" aria-label="Card front">
  <div class="wordmark">
    <div class="wordmark__name"><span>TRELLWICK</span><span class="wordmark__dot"></span></div>
    <div class="wordmark__sub">CONSTRUCTION GROUP LTD</div>
  </div>

  <div class="gallery">
    <div class="gallery__photo gallery__photo--fence" role="img" aria-label="Photo of a new timber fence beside a garden path"></div>
    <div class="gallery__photo gallery__photo--alley" role="img" aria-label="Photo of a resurfaced access lane between buildings"></div>
    <div class="gallery__photo gallery__photo--wall" role="img" aria-label="Photo of drainage works along a building wall"></div>
    <div class="gallery__photo gallery__photo--deck" role="img" aria-label="Photo of a finished timber deck with fencing"></div>
    <div class="gallery__photo gallery__photo--site" role="img" aria-label="Photo of groundworks at an industrial unit with a mini digger"></div>
  </div>

  <p class="services">
    Groundworks <span class="services__sep">•</span> Foundations <span class="services__sep">•</span> Drainage <span class="services__sep">•</span> Landscaping<br>
    Hard Landscaping <span class="services__sep">•</span> Patios <span class="services__sep">•</span> Decking <span class="services__sep">•</span> Fencing
  </p>
</section>

<section class="card card--back" aria-label="Card back">
  <svg class="back-art" width="694" height="400" viewBox="0 0 694 400" aria-hidden="true">
    <polygon points="0,0 272,0 302,42 0,72" fill="var(--grey-shape)"/>
    <polygon points="0,110 0,400 360,400" fill="var(--orange)"/>
  </svg>

  <div class="wordmark">
    <div class="wordmark__name"><span>TRELLWICK</span><span class="wordmark__dot"></span></div>
    <div class="wordmark__sub">CONSTRUCTION GROUP LTD</div>
  </div>

  <div class="contact">
    <div class="contact__name">NAME SURNAME</div>
    <div class="contact__title">Title</div>
    <div class="contact__icons">
      <svg class="contact__icon" viewBox="0 0 24 24" aria-label="Phone" role="img">
        <circle cx="12" cy="12" r="12" fill="var(--ink)"/>
        <path d="M8.2 6.5c.5-.4 1.1-.3 1.4.2l1.2 1.9c.3.5.2 1-.2 1.3l-.8.6c.6 1.4 1.6 2.5 3 3.2l.6-.8c.3-.4.9-.5 1.3-.2l1.9 1.2c.5.3.6 1 .2 1.4l-.9 1c-.6.6-1.5.8-2.3.5-3-1.2-5.2-3.5-6.3-6.4-.3-.8-.1-1.7.5-2.3z" fill="#fff"/>
      </svg>
      <svg class="contact__icon" viewBox="0 0 24 24" aria-label="Email" role="img">
        <circle cx="12" cy="12" r="12" fill="var(--ink)"/>
        <rect x="5.5" y="7.5" width="13" height="9" fill="none" stroke="#fff" stroke-width="1.4"/>
        <path d="M5.8 8l6.2 5 6.2-5" fill="none" stroke="#fff" stroke-width="1.4"/>
      </svg>
    </div>
    <div class="contact__line">07931 258 904 / 07713 829 516</div>
    <div class="contact__line">trellgroup@stonevane-mail.com</div>
  </div>
</section>

</body>
</html>
```